Company document Header needed

Using our current logo, I need a Designer to create a header for use on our company documents. This header will include our business address, phone, fax, website address

Reason: Dear designers, I am so pleased with the many different options that have been presented, that I wish to purchase several of them from a few different designers. I will get with the pixel forum folks and figure out what is the best way to do this. In the meantime, I am extending the deadline to allow for a few edits such as our phone number and such. thanks to you all for your excellent work. RT

Designers,

Please take a look and edit any of your submissions that have incorrect info on them:  the correct info is below:

Business name is: Brass Kite, Inc.

website address is:  www.brasskite-example.com

Office #:  (855) BrassKite  

Fax#:  (858) 516-2947  (generally I do not intend to need this on any materials unless it balances a look)

email:  info@brasskite-example.com

Address:  782 Larkwood Blvd. suite 2310  San Diego, CA  92174

Thanks!

```html
<!DOCTYPE html>
<html lang="en">
<head>
<meta charset="UTF-8">
<title>Brass Kite, Inc. — Letterhead</title>
<link rel="stylesheet" href="https://fonts.googleapis.com/css2?family=Barlow+Condensed:wght@600&family=Open+Sans:wght@400;700&display=swap">
<style>
  :root {
    --page: #ffffff;
    --band-dark: #141d4c;
    --band-mid: #1a4f86;
    --band-light: #1a8cc4;
    --brand-blue: #2a93cf;
    --text-light: #dfe8f2;
    --text-white: #ffffff;
    --mark: #d8e4f0;
  }
  html, body {
    margin: 0;
    padding: 0;
    width: 927px;
    height: 1200px;
    overflow: hidden;
    background: var(--page);
  }
  .letterhead {
    position: relative;
    width: 927px;
    height: 1200px;
    background: var(--page);
  }
  .header-band {
    position: absolute;
    left: 33px;
    top: 28px;
    width: 891px;
    height: 95px;
    background: linear-gradient(90deg, var(--band-dark) 0%, var(--band-dark) 12%, var(--band-mid) 55%, var(--band-light) 100%);
    font-family: "Open Sans", Arial, sans-serif;
  }
  .brand-square {
    position: absolute;
    left: 26px;
    top: 17px;
    width: 60px;
    height: 60px;
    background: var(--mark);
  }
  .brand-name {
    position: absolute;
    left: 118px;
    top: 17px;
    margin: 0;
    font-family: "Barlow Condensed", "Arial Narrow", sans-serif;
    font-weight: 600;
    font-size: 36px;
    line-height: 1;
    letter-spacing: 0.3px;
    color: var(--brand-blue);
    white-space: nowrap;
  }
  .brand-web {
    position: absolute;
    left: 118px;
    top: 64px;
    font-size: 10.5px;
    letter-spacing: 0.6px;
    color: var(--brand-blue);
    white-space: nowrap;
  }
  .address {
    position: absolute;
    left: 297px;
    top: 18px;
    margin: 0;
    font-style: normal;
    font-size: 14px;
    line-height: 20px;
    letter-spacing: 0.4px;
    color: var(--text-light);
    white-space: nowrap;
  }
  .email {
    position: absolute;
    left: 297px;
    top: 62px;
    font-size: 13px;
    font-weight: 700;
    color: var(--text-white);
    white-space: nowrap;
  }
  .phone-fax {
    position: absolute;
    left: 507px;
    top: 63px;
    font-size: 12px;
    font-weight: 700;
    letter-spacing: 0.9px;
    color: var(--text-white);
    white-space: nowrap;
  }
  .phone-fax .fax { margin-left: 10px; }
</style>
</head>
<body>
  <div class="letterhead">
    <header class="header-band">
      <div class="brand-square" aria-hidden="true"></div>
      <h1 class="brand-name">BRASS KITE</h1>
      <div class="brand-web">www.brasskite-example.com</div>
      <address class="address">
        782 Larkwood Blvd. suite 2310<br>
        San Diego, CA 92174
      </address>
      <div class="email">info@brasskite-example.com</div>
      <div class="phone-fax">
        <span class="phone">Phone 855BRASSKITE</span>
        <span class="fax">Fax 858-516-2947</span>
      </div>
    </header>
  </div>
</body>
</html>
```